First Annual Pemberton Family Reunion

Family reunion invitation, please see the attached letter for the language. Also provided a picture of my grandparents, if you could include it on a letter or brochure. I'm flexible.
Updates

I just uploaded a Word document with the time, address, and list of activities. Please click on the hyperlink, it takes you directly to our Family Reunion webpage and click on Agenda for all details.

Target Market(s)

Family and Friends invitation

Requirements
Must have
• Date, time, picture, family logo, and website for payment

```html
<!DOCTYPE html>
<html lang="en">
<head>
<meta charset="UTF-8">
<title>Pemberton Family Reunion – Invitation Letter</title>
<link href="https://fonts.googleapis.com/css2?family=Jost:wght@400;600&family=Archivo+Black&display=swap" rel="stylesheet">
<style>
  :root {
    --backdrop: #e6e7e6;
    --paper: #ffffff;
    --ink: #0a0a0a;
    --purple: #573093;
    --logo-paper: #fdfbf8;
    --rule: #9a9a9a;
  }
  * { box-sizing: border-box; margin: 0; padding: 0; }
  html, body {
    width: 1149px; height: 1200px; overflow: hidden;
    background: var(--backdrop);
  }
  .letter {
    position: absolute; left: 242px; top: 170px;
    width: 666px; height: 861px;
    background: var(--paper);
    border-left: 1px solid var(--rule);
    border-right: 1px solid var(--rule);
    font-family: "Jost", "Futura", sans-serif;
    color: var(--ink);
  }
  .bar { position: absolute; left: -1px; right: -1px; height: 15px; background: var(--ink); }
  .bar--top { top: 0; }
  .bar--bottom { top: 846px; }
  .header-band {
    position: absolute; left: -1px; right: -1px; top: 15px; height: 314px;
    background: var(--purple);
  }
  .family-mark {
    position: absolute; left: 271px; top: 0; width: 123px; height: 122px;
    background: var(--logo-paper);
    display: flex; align-items: center; justify-content: center; text-align: center;
    font-family: "Jost", sans-serif; font-weight: 600; font-size: 17px; line-height: 1.15;
    color: var(--ink); padding: 10px;
  }
  .date-ribbon { position: absolute; left: 183px; top: 130px; width: 294px; height: 43px; }
  .date-ribbon svg { position: absolute; inset: 0; }
  .date-ribbon span {
    position: absolute; inset: 0; display: flex; align-items: center; justify-content: center;
    font-family: "Archivo Black", sans-serif; font-size: 27px; color: #fff; letter-spacing: 0.5px;
  }
  .photo {
    position: absolute; top: 185px; width: 199px; height: 200px;
    border: 5px solid var(--ink);
  }
  .photo--grandparents { left: 24px; background: linear-gradient(160deg, #d9a65a 0%, #7a5a48 45%, #2e2a30 100%); }
  .photo--gathering { left: 234px; background: linear-gradient(170deg, #c9b99a 0%, #6b3a3a 50%, #1e1a1c 100%); }
  .photo--outdoors { left: 443px; background: linear-gradient(180deg, #4f6b3a 0%, #8a5a50 55%, #a59a88 100%); }
  .greeting {
    position: absolute; left: 30px; top: 417px;
    font-family: "Archivo Black", sans-serif; font-size: 23px; letter-spacing: 0.3px;
  }
  .letter-body {
    position: absolute; left: 23px; top: 457px; width: 612px;
    font-size: 13.2px; line-height: 16px;
  }
  .letter-body p { margin-bottom: 17px; }
  .letter-body strong { font-weight: 600; }
  .sign-off { margin-bottom: 0; }
  .sign-off strong { font-weight: 600; text-transform: uppercase; font-size: 12.5px; }
</style>
</head>
<body>
  <article class="letter">
    <div class="header-band"></div>
    <div class="bar bar--top"></div>
    <div class="family-mark">Pemberton Family Reunion</div>

    <div class="date-ribbon">
      <svg viewBox="0 0 294 43" width="294" height="43" aria-hidden="true">
        <polygon points="0,0 294,0 284,21.5 294,43 0,43 10,21.5" fill="#0a0a0a"/>
      </svg>
      <span>APRIL 7, 2023</span>
    </div>

    <div class="photo photo--grandparents" role="img" aria-label="Photo of the grandparents together"></div>
    <div class="photo photo--gathering" role="img" aria-label="Photo of family members gathered indoors"></div>
    <div class="photo photo--outdoors" role="img" aria-label="Photo of two family members outdoors"></div>

    <h1 class="greeting">DEAR FAMILY,</h1>

    <div class="letter-body">
      <p>I hope this letter finds all of you in good health and high spirits. Our family, which is spread across different parts of the country, rarely gets an opportunity to gather together under one roof, but I am excited to inform you that we have finally planned a family reunion.</p>
      <p>It has been long overdue, and we are looking forward to catching up with everyone, reminiscing old memories, and creating some new ones over the course of this event. I cannot emphasize enough on how important this reunion will be for our family. We have come to learn over the years that nothing can ever replace the love and connections that we share between us.</p>
      <p>Our family reunion will be from <strong>September 1, 2023,</strong> through <strong>September 3, 2023</strong>. We will have a fun-filled weekend filled with activities for all ages, which will include games, music, storytelling, and much more. It is a chance for our family to get to know new members, spend time with those we know and love, and to make it a memorable experience.</p>
      <p>Please RSVP and pay your deposit as soon as possible at https://pembertonreunion.net so that we can make arrangements accordingly. Also, please notify any family members who may have been left out or forgotten.</p>
      <p>I cannot wait to see all of you soon and spend quality time together as a family.</p>
      <p class="sign-off">As ever,<br><strong>The Pemberton’s Family Committee</strong></p>
    </div>

    <div class="bar bar--bottom"></div>
  </article>
</body>
</html>
```